Microlight Aircraft Website Project

Need a website designed, or at least a template made, that my web programmer can work with here. We are a new manufacturer of microlight aircraft & powered hang gliders. Our company name is Bright Fern. We manufacture portable utility aircraft in the Light Sport category (formerly known as Ultralights or Microlights). Our particular design is a 2-seat powered hang glider and caters to those who want to go explore the backcountry. We are not necessarily aviation nuts, but more into the development of a flying utility vehicle for extreme exploration and expeditions. We have been importing these aircraft from 3 countries for 15 years and have supplied over 200 expedition-quality aircraft world-wide. We are now manufacturing here in the US.

Industry/Entity Type

Manufacturer

Coding

Coded - Design and coding required

```html
<!DOCTYPE html>
<html lang="en">
<head>
<meta charset="utf-8">
<title>Bright Fern — Microlight Aircraft &amp; Powered Hang Gliders</title>
<link rel="stylesheet" href="https://fonts.googleapis.com/css2?family=Open+Sans:wght@400;600;700;800&display=swap">
<style>
:root{
  --navy:#0b4c9c;
  --navy-dark:#083d80;
  --sky:#1db9e9;
  --ink:#1d1d1d;
  --muted:#7a7a7a;
  --page:#f4f4f4;
  --white:#ffffff;
  --footer:#101a28;
  --footer-line:#24324a;
  --footer-text:#8a93a3;
}
*{box-sizing:border-box;margin:0;padding:0}
html,body{width:1200px;height:2571px;overflow:hidden}
body{font-family:"Open Sans",Arial,sans-serif;color:var(--ink);background:var(--page);position:relative}
a{color:inherit;text-decoration:none}
ul{list-style:none}

/* top bar */
.topbar{position:absolute;top:0;left:0;width:1200px;height:29px;background:var(--navy);color:var(--white);font-size:11px}
.topbar-links{position:absolute;left:168px;top:7px;display:flex;gap:10px}
.topbar-links span.sep{opacity:.7}
.topbar-contact{position:absolute;left:640px;top:7px;display:flex;gap:18px;align-items:center}
.topbar-contact span{display:flex;align-items:center;gap:4px}
.topbar-social{position:absolute;left:934px;top:3px;display:flex;gap:6px}
.topbar-social i{display:block;width:22px;height:22px;border-radius:50%;background:var(--sky)}

/* nav */
.nav{position:absolute;top:29px;left:0;width:1200px;height:72px;background:linear-gradient(90deg,var(--white) 0 330px,#f0f0f0 380px)}
.nav::before{content:"";position:absolute;left:330px;top:0;width:60px;height:72px;background:var(--white);clip-path:polygon(0 0,0 100%,100% 100%)}
.brand{position:absolute;left:168px;top:23px;display:flex;align-items:center;gap:8px;font-size:20px;font-weight:700;color:var(--navy);z-index:1}
.brand i{display:block;width:16px;height:16px;border-radius:50%;background:var(--navy)}
.menu{position:absolute;left:408px;top:0;display:flex;height:72px;font-size:11px;font-weight:700;color:#333;z-index:1}
.menu a{display:flex;align-items:center;padding:0 22px;height:72px}
.menu a.active{background:var(--navy);color:var(--white);padding:0 24px}

/* hero */
.hero{position:absolute;top:101px;left:0;width:1200px;height:495px;
  background:linear-gradient(180deg,#f6f4f2 0%,#f2e6da 12%,#c95a1d 30%,#d4511a 55%,#8f2c10 80%,#c84a1a 100%)}

/* welcome */
.section-title{text-align:center;font-size:28px;font-weight:600;letter-spacing:.5px;color:var(--ink)}
.section-title b{color:var(--navy);font-weight:800}
.section-sub{text-align:center;font-size:10.5px;letter-spacing:1px;color:var(--muted);text-transform:uppercase}
.welcome{position:absolute;top:596px;left:0;width:1200px;height:549px;background:var(--page)}
.welcome .section-title{position:absolute;top:46px;width:100%}
.welcome .section-sub{position:absolute;top:94px;width:100%}
.experts-photo{position:absolute;left:168px;top:153px;width:420px;height:319px;border:3px solid var(--navy);
  background:linear-gradient(180deg,#c9d3dc 0%,#8ea4b8 45%,#5f7690 100%)}
.experts-panel{position:absolute;left:567px;top:187px;width:465px;height:311px;border:3px solid var(--navy);background:var(--white);padding:32px 60px 0 70px}
.experts-heading{position:absolute;left:107px;top:-22px;width:250px;height:38px;border:3px solid var(--navy);background:var(--white);
  display:flex;align-items:center;justify-content:center;font-size:21px;font-weight:800;color:var(--navy);letter-spacing:.5px}
.experts-panel p{font-size:11px;line-height:17px;color:#555}
.feature{display:flex;gap:18px;margin-top:18px}
.feature-icon{flex:0 0 54px;height:48px;background:var(--navy);margin-top:10px;display:flex;align-items:center;justify-content:center}
.feature h4{font-size:11px;font-weight:700;letter-spacing:.5px;margin-bottom:6px}

/* band */
.band{position:absolute;top:1145px;left:0;width:1200px;height:274px;background:var(--sky);color:var(--white);text-align:center}
.band h2{position:absolute;top:60px;width:100%;font-size:26px;font-weight:700;letter-spacing:.5px}
.band h2 b{color:var(--navy);font-weight:800}
.band p{position:absolute;top:105px;left:243px;width:714px;font-size:18px;line-height:26px}
.band .btn{position:absolute;left:552px;top:197px;width:96px;height:29px;background:var(--navy);font-size:10px;font-weight:600;
  display:flex;align-items:center;justify-content:center}

/* packages */
.packages{position:absolute;top:1419px;left:0;width:1200px;height:621px;background:var(--page)}
.packages .section-title{position:absolute;top:44px;width:100%}
.packages .section-sub{position:absolute;top:90px;width:100%}
.card{position:absolute;top:148px;width:273px;height:425px;background:var(--white)}
.card-photo{height:142px;border:3px solid var(--navy)}
.card-photo.silver{background:linear-gradient(180deg,#9fc2dc 0%,#6e8f7a 60%,#3d5f7a 100%)}
.card-photo.gold{background:linear-gradient(180deg,#5d86ad 0%,#8fb2cf 60%,#b6cbdc 100%)}
.card-photo.platinum{background:linear-gradient(180deg,#cfe2f2 0%,#a9c7dd 50%,#6f9a45 75%,#5a8a35 100%)}
.card-body{padding:16px 30px 0}
.card h3{font-size:17px;font-weight:700;letter-spacing:1px}
.card .tag{font-size:10px;color:var(--muted);letter-spacing:.5px;margin-top:2px}
.price{margin-top:14px;font-size:24px;font-weight:800;color:var(--navy)}
.price small{font-size:9px;font-weight:700;margin-left:2px}
.card ul{margin-top:10px}
.card li{display:flex;align-items:center;gap:10px;font-size:11px;color:#555;height:31px}
.card .signup{position:absolute;left:0;bottom:0;width:273px;height:43px;background:var(--navy);color:var(--white);font-size:11px;
  display:flex;align-items:center;justify-content:center}

/* footer */
.footer{position:absolute;top:2040px;left:0;width:1200px;height:531px;background:var(--footer);color:var(--footer-text)}
.info-box{position:absolute;top:68px;width:273px;height:124px;border:3px solid var(--navy);padding:30px 50px 0 24px}
.info-icon{position:absolute;left:21px;top:-22px;width:36px;height:36px;background:var(--navy);display:flex;align-items:center;justify-content:center}
.info-box h4{color:var(--white);font-size:12px;font-weight:700;margin-bottom:8px}
.info-box p{font-size:11px;line-height:18px}
.footer-brand{position:absolute;left:168px;top:254px;display:flex;align-items:center;gap:8px;font-size:20px;font-weight:700;color:var(--white)}
.footer-brand i{display:block;width:16px;height:16px;border-radius:50%;background:var(--white)}
.footer-about{position:absolute;left:168px;top:312px;width:200px;font-size:9px;line-height:14px}
.footer-social{position:absolute;left:168px;top:377px;display:flex;gap:16px}
.footer-social i{display:block;width:22px;height:22px;border:1px solid var(--footer-text)}
.footer-col{position:absolute;top:228px;width:200px}
.footer-col h5{color:var(--white);font-size:11px;font-weight:700;padding-bottom:12px;position:relative}
.footer-col h5::after{content:"";position:absolute;left:0;bottom:0;width:30px;height:2px;background:var(--navy)}
.footer-col li{font-size:10px;height:31px;display:flex;align-items:center;border-bottom:1px solid var(--footer-line)}
.footer-col li::before{content:"›";margin-right:8px}
.hours li{display:block;height:48px;padding-top:8px}
.hours li::before{content:none}
.hours b{display:block;color:var(--white);font-size:10px;font-weight:600}
.copyright{position:absolute;left:0;top:2542px;width:1200px;text-align:center;font-size:9px;color:var(--white)}
</style>
</head>
<body>

<header class="topbar">
  <div class="topbar-links"><a>FAQ</a><span class="sep">|</span><a>Help Desk</a><span class="sep">|</span><a>Support</a></div>
  <div class="topbar-contact">
    <span><svg width="10" height="10" viewBox="0 0 24 24"><path fill="#fff" d="M6.6 10.8a15 15 0 0 0 6.6 6.6l2.2-2.2c.3-.3.7-.4 1-.2 1.1.4 2.3.6 3.6.6.6 0 1 .4 1 1V20c0 .6-.4 1-1 1A17 17 0 0 1 3 4c0-.6.4-1 1-1h3.5c.6 0 1 .4 1 1 0 1.3.2 2.5.6 3.6.1.3 0 .7-.2 1z"/></svg>555-014-2280</span>
    <span><svg width="11" height="9" viewBox="0 0 24 18"><rect x="1" y="1" width="22" height="16" fill="none" stroke="#fff" stroke-width="2"/><path d="M1 1l11 9 11-9" fill="none" stroke="#fff" stroke-width="2"/></svg>hello@brightfern.example</span>
  </div>
  <div class="topbar-social"><i></i><i></i><i></i><i></i></div>
</header>

<nav class="nav">
  <div class="brand"><i></i>Bright Fern</div>
  <div class="menu">
    <a class="active">HOME</a><a>ABOUT</a><a>SERVICES</a><a>PRODUCTS</a><a>PRICING</a><a>BLOG</a><a>CONTACT</a>
  </div>
</nav>

<section class="hero" role="img" aria-label="Powered hang glider with two pilots flying over red canyon rock formations"></section>

<section class="welcome">
  <h1 class="section-title"><b>WELCOME TO</b> BRIGHT FERN</h1>
  <p class="section-sub">Manufacturer of microlight aircraft &amp; powered hang gliders</p>
  <div class="experts-photo" role="img" aria-label="Red two-seat powered hang glider in flight above the clouds"></div>
  <div class="experts-panel">
    <div class="experts-heading">WE THE EXPERTS</div>
    <p>Lorem ipsum dolor sit amet, consectetur adipisicing elit. Animi praesentium saepe, consectetur consequatur deserunt, iusto eos aspernatur labore minus odit, est! Voluptatem alias eos ut voluptatum eum numquam eligendi fuga minima possimus!</p>
    <div class="feature">
      <div class="feature-icon"><svg width="24" height="24" viewBox="0 0 24 24"><circle cx="9" cy="5" r="3" fill="#fff"/><path d="M7 9h4v7h6v3H7z" fill="#fff"/></svg></div>
      <div><h4>TIPS AND ADVICE</h4><p>Lorem ipsum dolor sit amet, consectetur adipiscing elit. Aliquam interdum diam tortor, egestas varius erat aliquam a.</p></div>
    </div>
    <div class="feature">
      <div class="feature-icon"><svg width="24" height="24" viewBox="0 0 24 24"><circle cx="9" cy="5" r="3" fill="#fff"/><path d="M7 9h4v7h6v3H7z" fill="#fff"/></svg></div>
      <div><h4>BEST PROGRAM</h4><p>Lorem ipsum dolor sit amet, consectetur adipiscing elit. Aliquam interdum diam tortor, egestas varius erat aliquam a.</p></div>
    </div>
  </div>
</section>

<section class="band">
  <h2>OVER <b>15 YEARS</b> PROVIDING THE BEST SERVICE</h2>
  <p>We have been importing these aircraft from 3 countries for 15 years and have supplied over 200 expedition-quality aircraft world-wide. We are now manufacturing here in the US!</p>
  <a class="btn">CONTACT US</a>
</section>

<section class="packages">
  <h2 class="section-title"><b>OUR</b> PACKAGES</h2>
  <p class="section-sub">Lorem ipsum dolor sit amet, consectetur adipisicing elit.</p>

  <article class="card" style="left:168px">
    <div class="card-photo silver" role="img" aria-label="Powered hang glider flying along a green coastline"></div>
    <div class="card-body">
      <h3>SILVER</h3><p class="tag">LOREM IPSUM DOLOR SIT</p>
      <p class="price">$35* /<small>ITEM</small></p>
      <ul>
        <li><svg width="9" height="8" viewBox="0 0 10 8"><path d="M1 4l3 3 5-6" fill="none" stroke="#0b4c9c" stroke-width="2"/></svg>Free Consultation</li>
        <li><svg width="9" height="8" viewBox="0 0 10 8"><path d="M1 4l3 3 5-6" fill="none" stroke="#0b4c9c" stroke-width="2"/></svg>Lorem lipsum</li>
        <li><svg width="9" height="8" viewBox="0 0 10 8"><path d="M1 4l3 3 5-6" fill="none" stroke="#0b4c9c" stroke-width="2"/></svg>24 Hour Support</li>
        <li><svg width="9" height="8" viewBox="0 0 10 8"><path d="M1 4l3 3 5-6" fill="none" stroke="#0b4c9c" stroke-width="2"/></svg>Package No #1214</li>
      </ul>
    </div>
    <a class="signup">SIGNUP</a>
  </article>

  <article class="card" style="left:464px">
    <div class="card-photo gold" role="img" aria-label="Red powered hang glider against a blue sky"></div>
    <div class="card-body">
      <h3>GOLD</h3><p class="tag">LOREM IPSUM DOLOR SIT</p>
      <p class="price">$75* /<small>ITEM</small></p>
      <ul>
        <li><svg width="9" height="8" viewBox="0 0 10 8"><path d="M1 4l3 3 5-6" fill="none" stroke="#0b4c9c" stroke-width="2"/></svg>Free Consultation</li>
        <li><svg width="9" height="8" viewBox="0 0 10 8"><path d="M1 4l3 3 5-6" fill="none" stroke="#0b4c9c" stroke-width="2"/></svg>Lorem lipsum</li>
        <li><svg width="9" height="8" viewBox="0 0 10 8"><path d="M1 4l3 3 5-6" fill="none" stroke="#0b4c9c" stroke-width="2"/></svg>24 Hour Support</li>
        <li><svg width="9" height="8" viewBox="0 0 10 8"><path d="M1 4l3 3 5-6" fill="none" stroke="#0b4c9c" stroke-width="2"/></svg>Package No #1215</li>
      </ul>
    </div>
    <a class="signup">SIGNUP</a>
  </article>

  <article class="card" style="left:759px">
    <div class="card-photo platinum" role="img" aria-label="Colourful powered hang glider parked on a grass airfield"></div>
    <div class="card-body">
      <h3>PLATINUM</h3><p class="tag">LOREM IPSUM DOLOR SIT</p>
      <p class="price">$99* /<small>ITEM</small></p>
      <ul>
        <li><svg width="9" height="8" viewBox="0 0 10 8"><path d="M1 4l3 3 5-6" fill="none" stroke="#0b4c9c" stroke-width="2"/></svg>Free Consultation</li>
        <li><svg width="9" height="8" viewBox="0 0 10 8"><path d="M1 4l3 3 5-6" fill="none" stroke="#0b4c9c" stroke-width="2"/></svg>Lorem lipsum</li>
        <li><svg width="9" height="8" viewBox="0 0 10 8"><path d="M1 4l3 3 5-6" fill="none" stroke="#0b4c9c" stroke-width="2"/></svg>24 Hour Support</li>
        <li><svg width="9" height="8" viewBox="0 0 10 8"><path d="M1 4l3 3 5-6" fill="none" stroke="#0b4c9c" stroke-width="2"/></svg>Package No #1214</li>
      </ul>
    </div>
    <a class="signup">SIGNUP</a>
  </article>
</section>

<footer class="footer">
  <div class="info-box" style="left:168px">
    <div class="info-icon"><svg width="14" height="16" viewBox="0 0 24 28"><path d="M12 1a9 9 0 0 0-9 9c0 7 9 17 9 17s9-10 9-17a9 9 0 0 0-9-9z" fill="#fff"/><circle cx="12" cy="10" r="3.5" fill="#0b4c9c"/></svg></div>
    <h4>ADDRESS</h4><p>48 Ridgeway Lane, Alder County, USA.</p>
  </div>
  <div class="info-box" style="left:464px">
    <div class="info-icon"><svg width="15" height="12" viewBox="0 0 24 18"><rect x="1" y="1" width="22" height="16" fill="none" stroke="#fff" stroke-width="2"/><path d="M1 1l11 9 11-9" fill="none" stroke="#fff" stroke-width="2"/></svg></div>
    <h4>MAIL US</h4><p>Get support via<br>email : help@brightfern.example</p>
  </div>
  <div class="info-box" style="left:759px">
    <div class="info-icon"><svg width="14" height="14" viewBox="0 0 24 24"><path fill="#fff" d="M6.6 10.8a15 15 0 0 0 6.6 6.6l2.2-2.2c.3-.3.7-.4 1-.2 1.1.4 2.3.6 3.6.6.6 0 1 .4 1 1V20c0 .6-.4 1-1 1A17 17 0 0 1 3 4c0-.6.4-1 1-1h3.5c.6 0 1 .4 1 1 0 1.3.2 2.5.6 3.6.1.3 0 .7-.2 1z"/></svg></div>
    <h4>PHONE / FAX</h4><p>+1 555 014 2280<br>+1 555 014 2281</p>
  </div>

  <div class="footer-brand"><i></i>Bright Fern</div>
  <p class="footer-about">Lorem ipsum dolor sit amet, consectetur adipisicing elit.Lorem ipsum dolor sit amet, consectetur adipisicing elit.Lorem ipsum dolor sit amet, consectetur adipisicing elit.</p>
  <div class="footer-social"><i></i><i></i><i></i><i></i></div>

  <div class="footer-col" style="left:389px">
    <h5>Pages</h5>
    <ul><li>About Us</li><li>Services</li><li>Products</li><li>Events</li><li>Blog</li><li>Contact</li></ul>
  </div>
  <div class="footer-col" style="left:612px">
    <h5>Quick Links</h5>
    <ul><li>Privacy Policy</li><li>Disclaimer</li><li>Terms of Use</li><li>Copyright Notice</li><li>Media Center</li></ul>
  </div>
  <div class="footer-col hours" style="left:833px">
    <h5>Opening Hours</h5>
    <ul>
      <li><b>Monday To Friday:</b>9:00 am to 9:00 pm</li>
      <li><b>Monday To Friday:</b>9:00 am to 9:00 pm</li>
      <li><b>Monday To Friday:</b>9:00 am to 9:00 pm</li>
    </ul>
  </div>
</footer>
<p class="copyright">Copyright ©2016 Bright Fern.</p>

</body>
</html>
```